" A ORBALI Sistemas de Controle Industriais (ORBALI) é uma empresa brasileira cujo foco é o desenvolvimento de sistemas de análise e medição de processos industriais através da utilização de visão computacional. A ORBALI tem por objetivo fornecer ao mercado produtos e soluções para controle avançado e otimização de processos industriais utilizando análise de imagens. ****Os produtos e soluções da ORBALI realizam análises online de qualidade do processo industrial permitindo um controle imediato e continuo do processo industrial pelo cliente. Este é um conceito que pode também ser mostrado na site. O mercado alvo da ORBALI é o mercado industrial, em especial o mercado de mineração onde a ORBALI oferece analisadores online de processos industriais e projetos especiais para controles avançados de processos, promovendo para seus clientes melhorias nos seus processos e ganhos de produtividade. Dentro de seu plano estratégico a ORBALI tem como meta se tornar um dos principais fornecedores de soluções inovadoras de sistemas de visão computacional no mercado nacional e se tornar um exportador destas soluções para América do Sul e outros mercados internacionais. "

```html
<!DOCTYPE html>
<html lang="pt-BR">
<head>
<meta charset="utf-8">
<title>ORBALI Sistemas de Controle Industriais</title>
<link href="https://fonts.googleapis.com/css2?family=Raleway:wght@400;500;600;700&family=Open+Sans:wght@400;600;700&display=swap" rel="stylesheet">
<style>
:root{
  --green:#5cb531;
  --green-dark:#3f9420;
  --green-light:#8fd35c;
  --header:#2b2b2b;
  --ink:#222;
  --muted:#555;
  --card:#ececec;
  --line:#d8d8d8;
  --white:#fff;
}
*{box-sizing:border-box;margin:0;padding:0}
html,body{width:1200px;height:1200px;overflow:hidden;background:var(--white);font-family:"Open Sans",sans-serif;color:var(--ink)}
.page{position:relative;width:1200px;height:1200px;overflow:hidden}

.site-header{position:absolute;left:0;top:0;width:1200px;height:80px;background:var(--header)}
.brand{position:absolute;left:145px;top:20px;display:flex;align-items:center;gap:10px;font-family:"Raleway",sans-serif;font-weight:700;font-size:34px;color:var(--white);letter-spacing:1px}
.brand-dot{width:34px;height:34px;border-radius:50%;background:var(--green)}
.main-nav{position:absolute;right:148px;top:28px;display:flex;gap:14px;font-family:"Raleway",sans-serif;font-weight:700;font-size:12.5px;color:var(--white);white-space:nowrap}
.main-nav span{padding:4px 6px}
.main-nav .active{border:1px solid var(--white)}

.hero{position:absolute;left:0;top:80px;width:1200px;height:364px;overflow:hidden}
.hero-photo{position:absolute;inset:0;background:linear-gradient(100deg,#cdd3d8 0%,#eef0f1 25%,#d9d4c8 50%,#b9a98a 75%,#8c7a5e 100%)}
.hero-ring{position:absolute;left:672px;top:-10px;width:490px;height:490px;border-radius:50%;border:26px solid var(--green);background:rgba(20,40,20,.55)}
.hero-title{position:absolute;left:715px;top:148px;font-family:"Raleway",sans-serif;font-weight:600;font-size:29px;color:var(--white);letter-spacing:.5px;white-space:nowrap}
.hero-text{position:absolute;left:715px;top:196px;width:365px;font-family:"Raleway",sans-serif;font-size:19px;line-height:24px;color:var(--white)}
.hero-text b{color:var(--green-light)}
.hero-dots{position:absolute;left:826px;top:300px;display:flex;gap:5px}
.hero-dots i{width:8px;height:8px;border-radius:50%;border:1px solid var(--white)}
.hero-dots i:first-child{background:var(--white)}
.hero-arrow{position:absolute;top:125px;width:38px;height:50px;background:var(--green);display:flex;align-items:center;justify-content:center}
.hero-arrow.prev{left:78px}
.hero-arrow.next{right:0}

.intro{position:absolute;left:0;top:448px;width:1200px;text-align:center}
.intro h1{font-family:"Raleway",sans-serif;font-weight:400;font-size:52px;color:var(--green)}
.intro h1 b{font-weight:600}
.intro p{margin:6px auto 0;width:700px;font-weight:700;font-size:19px;line-height:27px;color:var(--ink)}

.card{position:absolute;top:595px;height:233px;background:var(--card);border-radius:8px;padding:20px 14px 0 14px}
.card.areas{left:149px;width:206px}
.card.about{left:413px;width:199px}
.card-head{display:flex;align-items:center;gap:12px;margin-bottom:14px}
.card-icon{width:42px;height:42px;border-radius:5px;background:var(--green);display:flex;align-items:center;justify-content:center;flex:none}
.card-title{font-family:"Raleway",sans-serif;font-weight:700;font-size:16px;line-height:18px;color:#333}
.card-text{font-size:9.5px;line-height:13.5px;color:var(--muted)}
.card-text+.card-text{margin-top:10px}
.btn-small{position:absolute;right:16px;bottom:14px;background:var(--green);color:var(--white);font-size:9px;font-weight:600;padding:4px 11px;border-radius:2px;white-space:nowrap}

.video{position:absolute;left:672px;top:595px;width:377px;height:233px;border-radius:6px;overflow:hidden}
.video-still{position:absolute;inset:0;background:linear-gradient(135deg,#c9a97a 0%,#a4703f 45%,#6f5a4a 75%,#3c3a3c 100%)}
.video-play{position:absolute;left:162px;top:78px;width:48px;height:48px;border-radius:50%;background:rgba(255,255,255,.92);display:flex;align-items:center;justify-content:center}
.video-bar{position:absolute;left:0;bottom:0;width:100%;height:30px;background:rgba(255,255,255,.95);display:flex;align-items:center;gap:8px;padding:0 10px;font-size:9px;color:#333;white-space:nowrap}
.video-track{flex:1;height:3px;background:#bbb}
.video-track i{display:block;width:55%;height:3px;background:var(--green)}

.divider{position:absolute;left:149px;top:852px;width:900px;height:1px;background:var(--line)}

.contact-title{position:absolute;left:149px;top:866px;font-family:"Raleway",sans-serif;font-weight:400;font-size:40px;color:var(--green);white-space:nowrap}
.contact-title b{font-weight:700}
.field{position:absolute;border:1px solid #bdbdbd;background:var(--white);font-size:9px;color:#444;padding:6px 8px}
.field.name{left:149px;top:926px;width:228px;height:29px}
.field.email{left:389px;top:926px;width:228px;height:29px}
.field.message{left:149px;top:970px;width:468px;height:106px}
.btn-send{position:absolute;left:149px;top:1084px;width:74px;height:27px;background:var(--green);color:var(--white);font-size:11px;font-weight:600;display:flex;align-items:center;justify-content:center;white-space:nowrap}

.info{position:absolute;top:950px;font-size:10.5px;line-height:15px;color:#444}
.info svg{display:block;margin-bottom:6px}
.info.address{left:640px;width:135px}
.info.phone{left:820px;white-space:nowrap}
.info.mail{left:948px;text-align:center;white-space:nowrap}

.site-footer{position:absolute;left:0;top:1123px;width:1200px;height:77px;background:linear-gradient(180deg,var(--green) 0%,var(--green-dark) 100%)}
.footer-nav{position:absolute;left:474px;top:18px;display:flex;gap:14px;font-family:"Raleway",sans-serif;font-weight:700;font-size:10px;color:var(--white);white-space:nowrap}
.copyright{position:absolute;left:760px;top:46px;font-size:11px;color:var(--white);white-space:nowrap}
.to-top{position:absolute;left:1006px;top:22px;width:30px;height:30px;border-radius:50%;border:2px solid var(--white);display:flex;align-items:center;justify-content:center}
</style>
</head>
<body>
<div class="page">

  <header class="site-header">
    <div class="brand"><span class="brand-dot"></span>ORBALI</div>
    <nav class="main-nav">
      <span class="active">HOME</span>
      <span>A EMPRESA</span>
      <span>TECNOLOGIA</span>
      <span>PRODUTOS &amp; SERVIÇOS</span>
      <span>CLIENTES &amp; PARCEIROS</span>
      <span>CONTATO</span>
    </nav>
  </header>

  <section class="hero">
    <div class="hero-photo" role="img" aria-label="Fotografia de plantas técnicas de engenharia com capacete de segurança e régua sobre a mesa"></div>
    <div class="hero-ring"></div>
    <h2 class="hero-title">TECNOLOGIA ORBALI</h2>
    <p class="hero-text">Desenvolvemos <b>equipamentos inovadores</b> de medição e análise para controle do processo industriais em tempo real.</p>
    <div class="hero-dots"><i></i><i></i><i></i><i></i><i></i></div>
    <div class="hero-arrow prev"><svg width="14" height="20" viewBox="0 0 14 20"><path d="M11 2 3 10l8 8" fill="none" stroke="#fff" stroke-width="3"/></svg></div>
    <div class="hero-arrow next"><svg width="14" height="20" viewBox="0 0 14 20"><path d="M3 2l8 8-8 8" fill="none" stroke="#fff" stroke-width="3"/></svg></div>
  </section>

  <section class="intro">
    <h1>Uma empresa <b>inovadora</b></h1>
    <p>Nosso foco é o desenvolvimento de sistemas de análise e medição de processos industriais através da utilização de visão computacional.</p>
  </section>

  <article class="card areas">
    <div class="card-head">
      <div class="card-icon"><svg width="26" height="26" viewBox="0 0 26 26" fill="none" stroke="#fff" stroke-width="2"><circle cx="13" cy="13" r="10"/><ellipse cx="13" cy="13" rx="4.5" ry="10"/><path d="M3 13h20"/></svg></div>
      <div class="card-title">ÁREAS<br>DE ATUAÇÃO</div>
    </div>
    <p class="card-text">Lorem ipsum dolor sit amet, consectetur adipiscing elit, sed do eiusmod tempor incididunt ut labore et dolore magna aliqua. Ut enim ad minim veniam, quis nostrud exercitation ullamco laboris nisi ut aliquip. Ut enim ad minim veniam, quis nostrud exercitation ullamco laboris nisi ut aliquip.</p>
    <span class="btn-small">Saiba mais</span>
  </article>

  <article class="card about">
    <div class="card-head">
      <div class="card-icon"><svg width="26" height="26" viewBox="0 0 26 26" fill="none" stroke="#fff" stroke-width="2"><rect x="3" y="4" width="20" height="14" rx="1"/><path d="M9 23h8M13 18v5"/></svg></div>
      <div class="card-title">O QUE<br>FAZEMOS?</div>
    </div>
    <p class="card-text">Lorem ipsum dolor sit amet, consectetur adipiscing elit, sed do eiusmod tempor incididunt ut labore et dolore magna aliqua.</p>
    <p class="card-text">Ut enim ad minim veniam, quis nostrud exercitation ullamco laboris nisi ut aliquip.</p>
    <span class="btn-small">Saiba mais</span>
  </article>

  <div class="video">
    <div class="video-still" role="img" aria-label="Quadro de vídeo com ilustração 3D de uma planta de mineração com correias transportadoras"></div>
    <div class="video-play"><svg width="18" height="20" viewBox="0 0 18 20"><path d="M3 2l13 8-13 8z" fill="#333"/></svg></div>
    <div class="video-bar">
      <svg width="10" height="10" viewBox="0 0 10 10"><path d="M1 1l8 4-8 4z" fill="#333"/></svg>
      <span>3:16 / 5:17</span>
      <div class="video-track"><i></i></div>
      <svg width="12" height="10" viewBox="0 0 12 10"><path d="M1 3h3l3-2v8L4 7H1z" fill="#333"/></svg>
    </div>
  </div>

  <div class="divider"></div>

  <h2 class="contact-title"><b>Fale conosco</b> agora mesmo !</h2>
  <div class="field name">Digite seu nome</div>
  <div class="field email">Digite seu email</div>
  <div class="field message">Digite sua mensagem</div>
  <div class="btn-send">Saiba mais</div>

  <div class="info address">
    <svg width="22" height="28" viewBox="0 0 22 28"><path d="M11 1a9 9 0 0 0-9 9c0 7 9 17 9 17s9-10 9-17a9 9 0 0 0-9-9z" fill="var(--green)"/><circle cx="11" cy="10" r="3.5" fill="#fff"/></svg>
    Rua das Palmeiras, 120, Bairro Centro, Vila Serena - São Paulo/Brasil
  </div>
  <div class="info phone">
    <svg width="30" height="26" viewBox="0 0 30 26"><path d="M3 9c0-4 5-6 12-6s12 2 12 6v2h-6V8H9v3H3z" fill="var(--green)"/><path d="M7 12h16l3 11H4z" fill="var(--green)"/><circle cx="15" cy="17" r="3" fill="#fff"/></svg>
    (21) 3400-1234<br>(21) 9 8000-4321
  </div>
  <div class="info mail">
    <svg width="32" height="24" viewBox="0 0 32 24" style="margin:0 auto 6px"><rect x="1" y="2" width="30" height="20" fill="var(--green)"/><path d="M1 2l15 11L31 2M1 22l11-10M31 22L20 12" fill="none" stroke="#fff" stroke-width="2"/></svg>
    contato@orbali.com.br
  </div>

  <footer class="site-footer">
    <nav class="footer-nav">
      <span>HOME</span><span>A EMPRESA</span><span>TECNOLOGIA</span><span>PRODUTOS &amp; SERVIÇOS</span><span>CLIENTES &amp; PARCEIROS</span><span>CONTATO</span>
    </nav>
    <p class="copyright">© todos os direitos reservados ORBALI.</p>
    <div class="to-top"><svg width="12" height="14" viewBox="0 0 12 14"><path d="M6 13V2M1 7l5-5 5 5" fill="none" stroke="#fff" stroke-width="2"/></svg></div>
  </footer>

</div>
</body>
</html>
```